Clean and modern business cards

Looking for an updated business card design for my dental office “corvanta dental” . Looking for a modern clean / sleek design . I’m thinking black background but open to seeing other options . One side needs to have an appointment card . Card needs to have logo, dentist name , phone, email , address . I’ve attached couple of cards I thought were cool as well as my logo
Target Market(s)
Dental patients
Industry/Entity Type
Dentistry
Contact Information for Business Card
Phone email address

```html
<!DOCTYPE html>
<html lang="en">
<head>
<meta charset="utf-8">
<title>Corvanta Dental – Business &amp; Appointment Card</title>
<link rel="stylesheet" href="https://fonts.googleapis.com/css2?family=Montserrat:wght@300;400;700;800;900&display=swap">
<style>
  :root{
    --backdrop:#d9d9d9;
    --card:#050505;
    --lime:#a6c91a;
    --lime-line:#6f8a10;
    --white:#ffffff;
    --field:#efefef;
    --ink:#050505;
  }
  *{box-sizing:border-box;margin:0;padding:0}
  html,body{width:1200px;height:846px;overflow:hidden}
  body{
    background:var(--backdrop);
    font-family:"Montserrat",sans-serif;
    position:relative;
  }
  .card{
    position:absolute;
    top:103px;
    width:400px;
    height:640px;
    background:var(--card);
    overflow:hidden;
    box-shadow:0 10px 24px rgba(0,0,0,.18);
  }
  .card--front{left:170px}
  .card--back{left:630px}

  .brand{
    display:flex;align-items:center;gap:14px;
    color:var(--white);
    font-weight:800;
    text-transform:uppercase;
    letter-spacing:.04em;
  }
  .brand__dot{
    border-radius:50%;
    background:var(--lime);
    flex:none;
  }
  .card--front .brand{
    position:absolute;top:70px;left:0;right:0;
    flex-direction:column;gap:18px;
    font-size:26px;text-align:center;line-height:1.15;
  }
  .card--front .brand__dot{width:150px;height:150px}

  .details{
    position:absolute;left:48px;right:40px;top:318px;
    color:var(--lime);
  }
  .details__name{font-weight:800;font-size:30px;line-height:1.1}
  .details__title{font-weight:300;font-size:19px;margin-top:4px}
  .rule{border:0;border-top:1px solid var(--lime-line);margin:16px 0}
  .contact{list-style:none;font-weight:300;font-size:17px}
  .contact li{display:flex;align-items:center;gap:12px;margin:6px 0}
  .contact svg{width:24px;height:20px;flex:none}
  .address{font-weight:300;font-size:17px;line-height:1.35}

  .band{
    position:absolute;left:0;right:0;bottom:0;height:92px;
    background:var(--lime);
    border-top:3px solid var(--card);
    box-shadow:inset 0 3px 0 var(--lime);
    display:flex;align-items:center;justify-content:center;
    color:var(--ink);font-weight:900;font-size:24px;letter-spacing:.02em;
  }
  .band::before{
    content:"";position:absolute;left:0;right:0;top:4px;border-top:2px solid var(--ink);
  }

  .card--back .brand{
    position:absolute;top:62px;right:36px;
    font-size:22px;
  }
  .card--back .brand__dot{width:70px;height:70px}
  .appointment{
    position:absolute;left:40px;right:40px;top:190px;
  }
  .appointment__heading{
    color:var(--lime);font-weight:900;font-size:23px;line-height:1.2;
    text-transform:uppercase;text-align:right;
  }
  .field{
    margin-top:18px;height:54px;border-radius:18px;
    background:var(--field);border:3px solid var(--lime);
    color:var(--lime);font-weight:800;font-size:19px;
    padding:10px 18px;
  }
  .appointment__heading + .field{margin-top:22px}
  .notice{
    margin-top:26px;color:var(--lime);font-weight:400;
    font-size:17px;line-height:1.3;
  }
</style>
</head>
<body>

<section class="card card--front" aria-label="Business card front">
  <div class="brand">
    <span class="brand__dot"></span>
    <span>Corvanta<br>Dental</span>
  </div>

  <div class="details">
    <h1 class="details__name">Dr Lenart</h1>
    <p class="details__title">BSc (dent) DMD</p>
    <hr class="rule">
    <ul class="contact">
      <li>
        <svg viewBox="0 0 24 20" aria-hidden="true"><path d="M6 2c1 0 3 4 3 5s-2 1.5-2 2.5 3 4.5 4 4.5 1.5-2 2.5-2 5 2 5 3-1.5 3-3.5 3C9 18 2 11 2 6c0-2 2-4 4-4z" fill="#a6c91a"/></svg>
        (204) 555-0182
      </li>
      <li>
        <svg viewBox="0 0 24 20" aria-hidden="true"><rect x="1" y="3" width="22" height="14" fill="#a6c91a"/><path d="M1 3l11 8 11-8" fill="none" stroke="#050505" stroke-width="1.6"/></svg>
        contact@corvantawpg.ca
      </li>
    </ul>
    <hr class="rule">
    <p class="address">210 – 4480 Larchmont Ave,<br>Winnipeg, MB R3K 2B7</p>
  </div>

  <div class="band">WWW.CORVANTAWPG.CA</div>
</section>

<section class="card card--back" aria-label="Appointment card">
  <div class="brand">
    <span class="brand__dot"></span>
    <span>Corvanta Dental</span>
  </div>

  <div class="appointment">
    <h2 class="appointment__heading">Your next<br>appointment is:</h2>
    <div class="field">Date</div>
    <div class="field">Time</div>
    <p class="notice">To cancel or reschedule please notify us at least 48 hours prior to your scheduled appointment</p>
  </div>

  <div class="band">WWW.CORVANTAWPG.CA</div>
</section>

</body>
</html>
```